Kesrow Consulting- executive coaching business

looking for business card design for a newly started coaching business.
specialising in Exective coaching, Leadership, NLP and Motivation.
Looking for a simple, classy design using the existing logo attached and colour themes that complement the logo.
No red or orange in the business card design please.

Target Market(s)

Defence and Veteran community

Industry/Entity Type

Life Coaching

Contact Information for Business Card

looking for business cards for newly started coaching business.
specialising in Exective Coaching, Leadership, NLP and Motivation

Font styles to use
Serif
Script

Colors
0556a4
3176b5
86cfc6
33b8a4

Requirements
Must have
• Logo
• Email address- Lena@kesrowconsulting.com.au
• Contact number
• Services provided - Executive Coaching, Leadership, NLP and Motivational Mapping.
Nice to have
• Same colours as logo
Should not have
• Red or orange

```html
<!DOCTYPE html>
<html lang="en">
<head>
<meta charset="utf-8">
<title>Kesrow Consulting – Business Card</title>
<link rel="stylesheet" href="https://fonts.googleapis.com/css2?family=Arimo:wght@400;700&family=Merriweather:wght@400&display=swap">
<style>
  :root {
    --page: #e9e8e5;
    --card-white: #f7f8f8;
    --card-black: #050505;
    --brand-blue: #1f6fbf;
    --brand-green: #2eaf6a;
    --ink: #1c1c1c;
    --rule: #222222;
    --back-text: #d9d9d9;
    --back-rule: #cfcfcf;
    --mark-grey: #9a9a9a;
  }
  * { box-sizing: border-box; margin: 0; padding: 0; }
  html, body {
    width: 1200px; height: 902px; overflow: hidden;
    background: var(--page);
    font-family: "Arimo", Arial, sans-serif;
  }
  .sheet {
    width: 1200px; height: 902px;
    display: flex; flex-direction: column; align-items: center; justify-content: center;
    gap: 44px;
  }
  .card {
    position: relative; width: 640px; height: 366px; overflow: hidden;
    box-shadow: 0 6px 18px rgba(0,0,0,0.18);
  }
  .brand { position: absolute; left: 0; right: 0; text-align: center; }
  .brand__mark {
    display: block; margin: 0 auto; border-radius: 50%;
    border: 3px solid currentColor;
  }
  .brand__name { display: block; font-weight: 700; letter-spacing: 1px; white-space: nowrap; }
  .brand__rule { display: block; height: 2px; margin: 10px auto 0; }

  /* Back side */
  .card--back { background: var(--card-black); color: var(--back-text); }
  .card--back .brand { top: 36px; }
  .card--back .brand__mark { width: 60px; height: 60px; color: #ffffff; }
  .card--back .brand__name { color: #ffffff; font-size: 30px; margin-top: 12px; }
  .card--back .brand__rule { width: 320px; background: var(--back-rule); }
  .services { position: absolute; left: 64px; top: 182px; }
  .services__title { font-family: "Merriweather", Georgia, serif; font-size: 28px; font-weight: 400; color: var(--brand-blue); margin-bottom: 6px; }
  .services__list { list-style: none; font-size: 18px; line-height: 28px; }
  .services__list li::before { content: "*"; color: var(--brand-green); font-weight: 700; margin-right: 14px; }

  /* Front side */
  .card--front { background: var(--card-white); }
  .card--front .brand { top: 20px; }
  .card--front .brand__mark { width: 60px; height: 60px; color: var(--mark-grey); }
  .card--front .brand__name { color: var(--brand-blue); font-size: 30px; margin-top: 8px; }
  .card--front .brand__rule { width: 300px; background: var(--brand-green); margin-top: 8px; }
  .swoosh { position: absolute; inset: 0; }
  .person { position: absolute; left: 60px; top: 176px; }
  .person__name { font-size: 24px; font-weight: 700; color: var(--brand-blue); }
  .person__title { font-size: 17px; color: var(--ink); margin-top: 2px; }
  .divider { position: absolute; left: 296px; top: 172px; width: 2px; height: 58px; background: var(--rule); }
  .contact { position: absolute; left: 316px; top: 170px; list-style: none; font-size: 15px; color: var(--ink); }
  .contact li { display: flex; align-items: center; gap: 10px; height: 30px; }
  .contact svg { width: 16px; height: 16px; flex: none; }
</style>
</head>
<body>
<main class="sheet">

  <section class="card card--back" aria-label="Card back">
    <div class="brand">
      <span class="brand__mark"></span>
      <span class="brand__name">KESROW CONSULTING</span>
      <span class="brand__rule"></span>
    </div>
    <div class="services">
      <h2 class="services__title">Services</h2>
      <ul class="services__list">
        <li>Executive Coaching</li>
        <li>Leadership</li>
        <li>NLP</li>
        <li>Motivational Mapping</li>
      </ul>
    </div>
  </section>

  <section class="card card--front" aria-label="Card front">
    <div class="brand">
      <span class="brand__mark"></span>
      <span class="brand__name">KESROW CONSULTING</span>
      <span class="brand__rule"></span>
    </div>

    <svg class="swoosh" viewBox="0 0 640 366" aria-hidden="true">
      <path d="M0 348 Q330 262 640 240 L640 256 Q330 276 0 360 Z" fill="var(--brand-green)"/>
      <path d="M0 366 L0 364 Q330 284 640 264 L640 366 Z" fill="var(--brand-blue)"/>
      <path id="addressPath" d="M170 352 Q400 306 620 290" fill="none"/>
      <text font-family="Arimo, Arial, sans-serif" font-size="15" fill="#ffffff">
        <textPath href="#addressPath">Fenwick Road, London, United Kingdom</textPath>
      </text>
    </svg>

    <div class="person">
      <p class="person__name">Martin Hallworth</p>
      <p class="person__title">Managing Director</p>
    </div>
    <span class="divider"></span>
    <ul class="contact">
      <li>
        <svg viewBox="0 0 16 16" aria-hidden="true"><rect width="16" height="16" rx="2" fill="var(--brand-green)"/><path d="M5 3.5 L7 6 L6 7 Q7 9 9 10 L10 9 L12.5 11 L11.5 12.5 Q6 12 3.5 5 Z" fill="#fff"/></svg>
        <span>555-014-2276</span>
      </li>
      <li>
        <svg viewBox="0 0 16 16" aria-hidden="true"><rect width="16" height="16" rx="2" fill="var(--brand-green)"/><rect x="3" y="4.5" width="10" height="7" fill="none" stroke="#fff" stroke-width="1.3"/><path d="M3 4.5 L8 8.5 L13 4.5" fill="none" stroke="#fff" stroke-width="1.3"/></svg>
        <span>Lena@kesrowconsulting.com.au</span>
      </li>
    </ul>
  </section>

</main>
</body>
</html>
```